Munchcart

App Design for a an application on which you can order take aways from restaurants close to you.
(similar app : https://appvault.example/lu/app/grubniq-pizza-burger-sushi/id583017264?l=en&mt=8 )

Logo is a taxi (psd of taxi an font attached)

Attached a draft mockup showing the screens needed.

Screens needed :

1. Splash Screen
2. Select you restaurant screen
3. Select your dish (meat, pizza, pasta....)
4. Select your extras (exta cheese, garlik etc...)
5. Exit screen with total amount and confirmation
6. Subscribe Screen where people have to register the first time.

Target Market(s)

age 14-54

Industry/Entity Type

Restaurant

Requirements
Must have
• Wood elements

```html
<!DOCTYPE html>
<html lang="en">
<head>
<meta charset="utf-8">
<title>Munchcart – Restaurant list</title>
<link href="https://fonts.googleapis.com/css2?family=Arimo:ital,wght@0,400;0,700;1,400&display=swap" rel="stylesheet">
<style>
  :root {
    --stage: #e4e4e4;
    --bezel: #0c0c0c;
    --denim: #1f2d40;
    --denim-dark: #162232;
    --stitch: #c9a55a;
    --sand: #d8cfba;
    --pill: #bdb39b;
    --wood-light: #d9a35f;
    --wood-dark: #b97b3c;
    --paper: #f4f4f2;
    --rule: #d6d6d3;
    --red: #d2151a;
    --grey: #7a7a7a;
    --blue: #2a8fd6;
    --chevron: #5fb2e6;
    --star: #f29b12;
    --icon: #c9ced6;
    --white: #ffffff;
    --photo-light: #e6d6c2;
    --photo-mid: #c99a72;
    --photo-dark: #7a4a2a;
  }
  * { box-sizing: border-box; margin: 0; padding: 0; }
  html, body { width: 1200px; height: 849px; overflow: hidden; }
  body {
    background: var(--stage);
    font-family: "Arimo", Arial, sans-serif;
    position: relative;
  }
  .screen {
    position: absolute;
    left: 380px; top: 30px;
    width: 440px; height: 790px;
    background: var(--bezel);
    display: flex; flex-direction: column;
    overflow: hidden;
  }
  .status-bar {
    height: 26px; flex: none; display: flex; align-items: center;
    padding: 0 10px; color: var(--white); font-weight: 700; font-size: 15px;
    position: relative;
  }
  .status-bar .carrier { display: flex; align-items: center; gap: 6px; }
  .status-bar .lock { position: absolute; left: 50%; transform: translateX(-50%); top: 5px; }
  .status-bar .battery { margin-left: auto; }
  .app-header {
    height: 58px; flex: none; background: linear-gradient(#263650, var(--denim));
    position: relative; display: flex; align-items: center; justify-content: center;
    border-radius: 6px 6px 0 0;
  }
  .app-header::before, .app-header::after {
    content: ""; position: absolute; left: 0; right: 0;
    border-top: 1px dashed var(--stitch);
  }
  .app-header::before { top: 5px; }
  .app-header::after { bottom: 5px; }
  .app-header h1 { color: var(--white); font-size: 24px; font-weight: 700; text-shadow: 0 -1px 0 #000; }
  .search-band {
    height: 56px; flex: none; background: var(--sand);
    display: flex; align-items: center; gap: 14px; padding: 0 14px 6px;
    position: relative; z-index: 2;
  }
  .search-band .zigzag { position: absolute; left: 0; bottom: -6px; }
  .search-field {
    flex: 1; height: 30px; border-radius: 15px; background: var(--pill);
    box-shadow: inset 0 1px 3px rgba(0,0,0,.35);
    display: flex; align-items: center; padding: 0 10px 0 28px;
    font-style: italic; font-size: 15px; color: #4a4538;
  }
  .search-field svg { margin-left: auto; }
  .list-area {
    flex: 1; min-height: 0;
    background: linear-gradient(90deg, var(--wood-dark), var(--wood-light) 20%, var(--wood-light) 80%, var(--wood-dark));
    padding: 0 20px;
  }
  .restaurant-list {
    list-style: none; background: var(--paper); height: 100%;
    box-shadow: 0 0 6px rgba(0,0,0,.35);
  }
  .restaurant {
    height: 106px; display: flex; align-items: center; gap: 10px;
    padding: 0 18px 0 6px; border-bottom: 1px solid var(--rule);
  }
  .restaurant .thumb {
    width: 80px; height: 80px; border-radius: 6px; flex: none;
    background: linear-gradient(170deg, var(--photo-light) 0%, var(--photo-mid) 55%, var(--photo-dark) 100%);
    box-shadow: 0 1px 3px rgba(0,0,0,.4);
  }
  .restaurant .info { flex: 1; line-height: 1; }
  .restaurant .name { color: var(--red); font-weight: 700; font-size: 14px; margin-bottom: 6px; }
  .restaurant .cuisine { color: var(--grey); font-style: italic; font-size: 12px; margin-bottom: 7px; }
  .restaurant .meta { color: var(--blue); font-weight: 700; font-size: 10.5px; display: flex; align-items: center; gap: 4px; margin-bottom: 7px; }
  .restaurant .meta .sep { width: 1px; height: 11px; background: #aaa; margin: 0 3px; }
  .restaurant .rating { display: flex; align-items: center; gap: 6px; font-size: 10.5px; font-style: italic; color: var(--grey); }
  .tab-bar {
    height: 70px; flex: none; background: var(--denim); display: flex;
    border-top: 1px solid #0a121c;
  }
  .tab {
    flex: 1; display: flex; flex-direction: column; align-items: center; justify-content: center; gap: 6px;
    color: var(--white); font-size: 12.5px; line-height: 1; border-left: 1px dashed var(--stitch);
  }
  .tab:first-child { border-left: none; }
  .tab.is-active { background: var(--denim-dark); }
  .tab-icon { height: 26px; display: flex; align-items: center; justify-content: center; }
</style>
</head>
<body>
<main class="screen">
  <div class="status-bar">
    <span class="carrier">
      <svg width="22" height="12" viewBox="0 0 22 12" fill="#fff"><rect x="0" y="8" width="3" height="4"/><rect x="4" y="6" width="3" height="6"/><rect x="8" y="4" width="3" height="8"/><rect x="12" y="2" width="3" height="10"/><rect x="16" y="0" width="3" height="12"/></svg>
      NORVA&nbsp;&nbsp;3G
    </span>
    <svg class="lock" width="12" height="15" viewBox="0 0 12 15"><path d="M3 7V4.5a3 3 0 0 1 6 0V7" fill="none" stroke="#fff" stroke-width="2"/><rect x="0" y="7" width="12" height="8" rx="1" fill="#fff"/></svg>
    <svg class="battery" width="28" height="13" viewBox="0 0 28 13"><rect x="0.5" y="0.5" width="24" height="12" rx="2" fill="none" stroke="#fff"/><rect x="2" y="2" width="21" height="9" fill="#fff"/><rect x="25" y="4" width="2.5" height="5" fill="#fff"/></svg>
  </div>

  <header class="app-header"><h1>Restaurant</h1></header>

  <div class="search-band">
    <svg width="26" height="34" viewBox="0 0 26 34"><path d="M13 0a13 13 0 0 1 13 13c0 9-13 21-13 21S0 22 0 13A13 13 0 0 1 13 0z" fill="#4a4a48"/><circle cx="13" cy="13" r="5" fill="var(--sand)"/></svg>
    <div class="search-field">Search
      <svg width="20" height="20" viewBox="0 0 20 20"><circle cx="12" cy="8" r="6" fill="none" stroke="#222" stroke-width="2"/><line x1="7.5" y1="12.5" x2="1.5" y2="18.5" stroke="#222" stroke-width="3" stroke-linecap="round"/></svg>
    </div>
    <svg class="zigzag" width="440" height="6" viewBox="0 0 440 6" preserveAspectRatio="none"><path d="M0 0 L4 6 L8 0 L12 6 L16 0 L20 6 L24 0 L28 6 L32 0 L36 6 L40 0 L44 6 L48 0 L52 6 L56 0 L60 6 L64 0 L68 6 L72 0 L76 6 L80 0 L84 6 L88 0 L92 6 L96 0 L100 6 L104 0 L108 6 L112 0 L116 6 L120 0 L124 6 L128 0 L132 6 L136 0 L140 6 L144 0 L148 6 L152 0 L156 6 L160 0 L164 6 L168 0 L172 6 L176 0 L180 6 L184 0 L188 6 L192 0 L196 6 L200 0 L204 6 L208 0 L212 6 L216 0 L220 6 L224 0 L228 6 L232 0 L236 6 L240 0 L244 6 L248 0 L252 6 L256 0 L260 6 L264 0 L268 6 L272 0 L276 6 L280 0 L284 6 L288 0 L292 6 L296 0 L300 6 L304 0 L308 6 L312 0 L316 6 L320 0 L324 6 L328 0 L332 6 L336 0 L340 6 L344 0 L348 6 L352 0 L356 6 L360 0 L364 6 L368 0 L372 6 L376 0 L380 6 L384 0 L388 6 L392 0 L396 6 L400 0 L404 6 L408 0 L412 6 L416 0 L420 6 L424 0 L428 6 L432 0 L436 6 L440 0 Z" fill="var(--sand)"/></svg>
  </div>

  <section class="list-area">
    <ul class="restaurant-list">
      <li class="restaurant">
        <div class="thumb" role="img" aria-label="Photo of the restaurant's pizza"></div>
        <div class="info">
          <p class="name">RESTAURANT NAME</p>
          <p class="cuisine">Italienische</p>
          <p class="meta"><svg width="10" height="10" viewBox="0 0 10 10"><circle cx="5" cy="5" r="4" fill="none" stroke="currentColor" stroke-width="1.4"/><path d="M5 2.5V5h2" fill="none" stroke="currentColor" stroke-width="1.2"/></svg>12.30 bis 22.30<span class="sep"></span><svg width="8" height="11" viewBox="0 0 8 11"><path d="M4 0a4 4 0 0 1 4 4c0 3-4 7-4 7S0 7 0 4a4 4 0 0 1 4-4z" fill="currentColor"/><circle cx="4" cy="4" r="1.5" fill="#fff"/></svg>2km away</p>
          <p class="rating"><svg width="62" height="12" viewBox="0 0 62 12" fill="var(--star)"><g id="stars"><polygon points="6,0 7.8,4 12,4.4 8.8,7.2 9.7,11.5 6,9.3 2.3,11.5 3.2,7.2 0,4.4 4.2,4"/><polygon transform="translate(12.5 0)" points="6,0 7.8,4 12,4.4 8.8,7.2 9.7,11.5 6,9.3 2.3,11.5 3.2,7.2 0,4.4 4.2,4"/><polygon transform="translate(25 0)" points="6,0 7.8,4 12,4.4 8.8,7.2 9.7,11.5 6,9.3 2.3,11.5 3.2,7.2 0,4.4 4.2,4"/><polygon transform="translate(37.5 0)" points="6,0 7.8,4 12,4.4 8.8,7.2 9.7,11.5 6,9.3 2.3,11.5 3.2,7.2 0,4.4 4.2,4"/><polygon transform="translate(50 0)" points="6,0 7.8,4 12,4.4 8.8,7.2 9.7,11.5 6,9.3 2.3,11.5 3.2,7.2 0,4.4 4.2,4"/></g></svg>( 80 review)</p>
        </div>
        <svg width="20" height="28" viewBox="0 0 20 28"><path d="M4 3 L15 14 L4 25" fill="none" stroke="var(--chevron)" stroke-width="5" stroke-linecap="round" stroke-linejoin="round"/></svg>
      </li>
      <li class="restaurant">
        <div class="thumb" role="img" aria-label="Photo of the restaurant's pizza"></div>
        <div class="info">
          <p class="name">RESTAURANT NAME</p>
          <p class="cuisine">Italienische</p>
          <p class="meta"><svg width="10" height="10" viewBox="0 0 10 10"><circle cx="5" cy="5" r="4" fill="none" stroke="currentColor" stroke-width="1.4"/><path d="M5 2.5V5h2" fill="none" stroke="currentColor" stroke-width="1.2"/></svg>12.30 bis 22.30<span class="sep"></span><svg width="8" height="11" viewBox="0 0 8 11"><path d="M4 0a4 4 0 0 1 4 4c0 3-4 7-4 7S0 7 0 4a4 4 0 0 1 4-4z" fill="currentColor"/><circle cx="4" cy="4" r="1.5" fill="#fff"/></svg>2km away</p>
          <p class="rating"><svg width="62" height="12" viewBox="0 0 62 12" fill="var(--star)"><use href="#stars"/></svg>( 80 review)</p>
        </div>
        <svg width="20" height="28" viewBox="0 0 20 28"><path d="M4 3 L15 14 L4 25" fill="none" stroke="var(--chevron)" stroke-width="5" stroke-linecap="round" stroke-linejoin="round"/></svg>
      </li>
      <li class="restaurant">
        <div class="thumb" role="img" aria-label="Photo of the restaurant's pizza"></div>
        <div class="info">
          <p class="name">RESTAURANT NAME</p>
          <p class="cuisine">Italienische</p>
          <p class="meta"><svg width="10" height="10" viewBox="0 0 10 10"><circle cx="5" cy="5" r="4" fill="none" stroke="currentColor" stroke-width="1.4"/><path d="M5 2.5V5h2" fill="none" stroke="currentColor" stroke-width="1.2"/></svg>12.30 bis 22.30<span class="sep"></span><svg width="8" height="11" viewBox="0 0 8 11"><path d="M4 0a4 4 0 0 1 4 4c0 3-4 7-4 7S0 7 0 4a4 4 0 0 1 4-4z" fill="currentColor"/><circle cx="4" cy="4" r="1.5" fill="#fff"/></svg>2km away</p>
          <p class="rating"><svg width="62" height="12" viewBox="0 0 62 12" fill="var(--star)"><use href="#stars"/></svg>( 80 review)</p>
        </div>
        <svg width="20" height="28" viewBox="0 0 20 28"><path d="M4 3 L15 14 L4 25" fill="none" stroke="var(--chevron)" stroke-width="5" stroke-linecap="round" stroke-linejoin="round"/></svg>
      </li>
      <li class="restaurant">
        <div class="thumb" role="img" aria-label="Photo of the restaurant's pizza"></div>
        <div class="info">
          <p class="name">RESTAURANT NAME</p>
          <p class="cuisine">Italienische</p>
          <p class="meta"><svg width="10" height="10" viewBox="0 0 10 10"><circle cx="5" cy="5" r="4" fill="none" stroke="currentColor" stroke-width="1.4"/><path d="M5 2.5V5h2" fill="none" stroke="currentColor" stroke-width="1.2"/></svg>12.30 bis 22.30<span class="sep"></span><svg width="8" height="11" viewBox="0 0 8 11"><path d="M4 0a4 4 0 0 1 4 4c0 3-4 7-4 7S0 7 0 4a4 4 0 0 1 4-4z" fill="currentColor"/><circle cx="4" cy="4" r="1.5" fill="#fff"/></svg>2km away</p>
          <p class="rating"><svg width="62" height="12" viewBox="0 0 62 12" fill="var(--star)"><use href="#stars"/></svg>( 80 review)</p>
        </div>
        <svg width="20" height="28" viewBox="0 0 20 28"><path d="M4 3 L15 14 L4 25" fill="none" stroke="var(--chevron)" stroke-width="5" stroke-linecap="round" stroke-linejoin="round"/></svg>
      </li>
      <li class="restaurant">
        <div class="thumb" role="img" aria-label="Photo of the restaurant's pizza"></div>
        <div class="info">
          <p class="name">RESTAURANT NAME</p>
          <p class="cuisine">Italienische</p>
          <p class="meta"><svg width="10" height="10" viewBox="0 0 10 10"><circle cx="5" cy="5" r="4" fill="none" stroke="currentColor" stroke-width="1.4"/><path d="M5 2.5V5h2" fill="none" stroke="currentColor" stroke-width="1.2"/></svg>12.30 bis 22.30<span class="sep"></span><svg width="8" height="11" viewBox="0 0 8 11"><path d="M4 0a4 4 0 0 1 4 4c0 3-4 7-4 7S0 7 0 4a4 4 0 0 1 4-4z" fill="currentColor"/><circle cx="4" cy="4" r="1.5" fill="#fff"/></svg>2km away</p>
          <p class="rating"><svg width="62" height="12" viewBox="0 0 62 12" fill="var(--star)"><use href="#stars"/></svg>( 80 review)</p>
        </div>
        <svg width="20" height="28" viewBox="0 0 20 28"><path d="M4 3 L15 14 L4 25" fill="none" stroke="var(--chevron)" stroke-width="5" stroke-linecap="round" stroke-linejoin="round"/></svg>
      </li>
    </ul>
  </section>

  <nav class="tab-bar">
    <div class="tab is-active">
      <span class="tab-icon"><svg width="28" height="24" viewBox="0 0 28 24"><rect x="1" y="1" width="26" height="7" rx="1" fill="var(--red)"/><rect x="3" y="9" width="22" height="14" fill="none" stroke="var(--red)" stroke-width="2.5"/><rect x="8" y="13" width="12" height="4" fill="var(--red)"/></svg></span>
      Restaurant
    </div>
    <div class="tab">
      <span class="tab-icon"><svg width="28" height="24" viewBox="0 0 28 24"><path d="M14 23 C4 15 1 11 1 7 A6 6 0 0 1 14 5 A6 6 0 0 1 27 7 C27 11 24 15 14 23 Z" fill="var(--icon)"/></svg></span>
      Favorites
    </div>
    <div class="tab">
      <span class="tab-icon"><svg width="28" height="24" viewBox="0 0 30 26"><path d="M9 10 L15 2 L21 10" fill="none" stroke="var(--icon)" stroke-width="2"/><rect x="1" y="10" width="28" height="4" fill="var(--icon)"/><path d="M3 15 H27 L25 25 H5 Z" fill="var(--icon)"/><path d="M10 17 V23 M15 17 V23 M20 17 V23" stroke="var(--denim)" stroke-width="1.6"/></svg></span>
      Check Out
    </div>
    <div class="tab">
      <span class="tab-icon"><svg width="32" height="24" viewBox="0 0 32 24" fill="var(--icon)"><circle cx="6" cy="12" r="3.5"/><circle cx="16" cy="12" r="3.5"/><circle cx="26" cy="12" r="3.5"/></svg></span>
      More
    </div>
  </nav>
</main>
</body>
</html>
```